Poster for a online company that buys your stuff

SwapKestrel offers a website which customers can get a instant offer for stuff their looking to sell. They then Courier the items in to us and they get paid the same day it arrives
We're looking for an eye catching design which portrays our hassle free process
We'll need your help to come up with a slogan/catch phrase and our easy 1,2,3 process so customers can see the poster and instantly have a clear understanding of what we do
1. Get an instant offer on our website
2. Send your item(s) to us
3.Get paid within 24 Hours
Industry/Entity Type
It Company
Look and feel
Each slider illustrates characteristics of the customer's brand and the style your logo design should communicate.

```html
<!DOCTYPE html>
<html lang="en">
<head>
<meta charset="utf-8">
<title>SwapKestrel – Sell Your Products Easily</title>
<link rel="stylesheet" href="https://fonts.googleapis.com/css2?family=Arimo:wght@400;700&display=swap">
<style>
  :root {
    --backdrop: #6b6b6b;
    --panel-grey: #dcdddd;
    --ink: #222222;
    --brand-green: #0a9a2a;
    --deep-green: #0c5f35;
    --mid-green: #07963a;
    --lime: #8dc63f;
    --icon-dark: #333333;
    --white: #ffffff;
  }
  * { box-sizing: border-box; margin: 0; padding: 0; }
  html, body {
    width: 900px; height: 1200px; overflow: hidden;
    background: var(--backdrop);
    font-family: "Arimo", Arial, sans-serif;
  }
  .poster {
    position: absolute; left: 133px; top: 155px;
    width: 632px; height: 892px;
    background: var(--panel-grey);
    overflow: hidden;
  }
  .poster-shapes { position: absolute; inset: 0; }
  .mascot-art {
    position: absolute; left: 187px; top: 15px; width: 310px; height: 270px;
    border-radius: 40% 45% 35% 40%;
    background: radial-gradient(ellipse at 55% 50%, #a7d46a 0%, #cfe3b4 45%, rgba(220,221,221,0) 72%);
  }
  .brand-name {
    position: absolute; left: 0; right: 0; top: 283px;
    text-align: center; font-weight: 700; font-size: 46px;
    color: #2b2b2b; letter-spacing: -1px;
  }
  .headline { position: absolute; left: 0; right: 0; text-align: center; }
  .headline-lead { top: 480px; font-size: 30px; color: var(--ink); }
  .headline-main { top: 513px; font-size: 82px; color: var(--brand-green); letter-spacing: 6px; line-height: 1; }
  .headline-sub { top: 602px; font-size: 33px; font-weight: 700; color: var(--brand-green); }
  .steps-connector { position: absolute; left: 0; top: 632px; width: 632px; height: 60px; }
  .step { position: absolute; top: 680px; width: 200px; text-align: center; }
  .step-number {
    position: absolute; top: -4px; font-size: 22px; color: var(--brand-green);
  }
  .step-icon { display: block; margin: 0 auto; }
  .step-caption { margin-top: 8px; font-size: 13.5px; line-height: 17px; color: var(--ink); }
  .call-bar { position: absolute; left: 0; bottom: 0; width: 632px; height: 60px; }
  .call-label {
    position: absolute; left: 38px; top: 842px; font-size: 38px; color: var(--white);
  }
  .call-number {
    position: absolute; left: 252px; top: 840px; font-size: 40px; font-weight: 700;
    color: var(--brand-green); letter-spacing: 1px;
  }
</style>
</head>
<body>
<main class="poster">
  <svg class="poster-shapes" viewBox="0 0 632 892" width="632" height="892" aria-hidden="true">
    <defs>
      <linearGradient id="lime-fade" x1="0" y1="0" x2="1" y2="0">
        <stop offset="0" stop-color="#8dc63f"/>
        <stop offset="1" stop-color="#2fa53a"/>
      </linearGradient>
    </defs>
    <polygon points="0,335 300,395 632,445 632,498 0,455" fill="var(--mid-green)"/>
    <polygon points="0,335 190,398 0,455" fill="url(#lime-fade)"/>
    <polygon points="280,390 632,318 632,440" fill="var(--deep-green)"/>
    <polygon points="280,390 632,440 632,460" fill="#9ccb2a"/>
    <polygon points="0,455 632,498 632,892 0,892" fill="var(--white)"/>
  </svg>

  <div class="mascot-art" role="img" aria-label="Cartoon courier mascot in green cap and overalls running with an orange parcel, giving a thumbs up"></div>
  <div class="brand-name">SwapKestrel</div>

  <h1 class="headline headline-lead" style="font-weight:400">SELL YOUR PRODUCTS</h1>
  <div class="headline headline-main">EASILY</div>
  <div class="headline headline-sub">IN 3 SIMPLE STEPS</div>

  <svg class="steps-connector" viewBox="0 0 632 60" aria-hidden="true">
    <path d="M322 0 V23 M132 23 H512 M132 23 V50 M322 23 V50 M512 23 V50" stroke="var(--brand-green)" stroke-width="1.2" fill="none"/>
  </svg>

  <div class="step" style="left:32px">
    <span class="step-number" style="left:47px">1</span>
    <svg class="step-icon" width="98" height="98" viewBox="0 0 98 98" aria-hidden="true">
      <circle cx="49" cy="49" r="48" fill="var(--lime)"/>
      <circle cx="49" cy="49" r="40" fill="var(--icon-dark)"/>
      <g stroke="#fff" stroke-width="2" fill="none">
        <circle cx="49" cy="49" r="22"/>
        <ellipse cx="49" cy="49" rx="10" ry="22"/>
        <path d="M27 49 H71 M49 27 V71 M31 38 H67 M31 60 H67"/>
      </g>
    </svg>
    <p class="step-caption">Get an instant<br>offer on our website</p>
  </div>

  <div class="step" style="left:222px">
    <span class="step-number" style="left:40px">2</span>
    <svg class="step-icon" width="98" height="98" viewBox="0 0 98 98" aria-hidden="true">
      <circle cx="49" cy="49" r="48" fill="var(--lime)"/>
      <circle cx="49" cy="49" r="40" fill="var(--icon-dark)"/>
      <g stroke="#fff" stroke-width="2" fill="none">
        <path d="M28 30 H33 V64 H70"/>
        <rect x="38" y="38" width="26" height="22"/>
        <path d="M45 38 V60 M51 38 V60 M57 38 V60"/>
        <circle cx="39" cy="69" r="3.5"/>
        <circle cx="64" cy="69" r="3.5"/>
      </g>
    </svg>
    <p class="step-caption">Send your<br>item(s) to us</p>
  </div>

  <div class="step" style="left:410px">
    <span class="step-number" style="left:32px">3</span>
    <svg class="step-icon" width="98" height="98" viewBox="0 0 98 98" aria-hidden="true">
      <circle cx="49" cy="49" r="48" fill="var(--lime)"/>
      <circle cx="49" cy="49" r="40" fill="var(--icon-dark)"/>
      <path d="M33 37 A22 22 0 1 1 33 61" stroke="#fff" stroke-width="3" fill="none"/>
      <path d="M27 33 L35 38 L29 44 Z" fill="#fff"/>
      <text x="58" y="45" fill="#fff" font-family="Arimo, Arial, sans-serif" font-size="14" text-anchor="middle">P</text>
      <text x="41" y="62" fill="#fff" font-family="Arimo, Arial, sans-serif" font-weight="700" font-size="15" text-anchor="middle">24h</text>
    </svg>
    <p class="step-caption">Get paid<br>within 24 Hours</p>
  </div>

  <svg class="call-bar" viewBox="0 0 632 60" aria-hidden="true">
    <polygon points="0,1 205,1 232,52 632,52 632,60 0,60" fill="var(--brand-green)"/>
    <polygon points="0,1 205,1 232,52 0,52" fill="#0b7f24"/>
  </svg>
  <div class="call-label">Call us:</div>
  <div class="call-number">077- 4821- 6039</div>
</main>
</body>
</html>
```